Graphic of Teacher Agility Framework

I need a model designed for my teacher educator agility framework. The concepts are responsive to each other on Figure 12 on the attachment and the text explains it all.

This is meant to be a conceptual framework of how ones thinks between experience, and theory, and research.

The domains represent a hierarchy of knowledge of specific domains that have enabled my learning to develop in-depth. I chose the term ‘agility framework’ to emphasise the importance of a responsiveness to the context and of the ability to respond with urgency between the various components (The Quillmark, 2012). I present the agility framework in Figure 12. The concentric circles are inter-connected as they are inter-dependent aspects of developing personal empowerment. The applicability of each domain relies on my ability to be aware of the context and to build work with urgency.

My learning has been iterative throughout this research, so this framework is intended to be understood as iterative, with movement between the concentric circles at a cognitive and behavioural level when greater awareness is gained. At the heart of the main circle are the researcherly dispositions that have been essential to my research and professional roles as well as to my personal learning. I have used descriptive headings for these dispositions that I believe are helpful for understanding them. The first one, ‘value deep understanding’, is modelled on Vostrup (2019); whilst ‘cognitive flexibility’ is an inter-cultural competency from Brasko et al (2014). I have also added in ‘responsiveness’ and ‘sensory awareness’ which I believe are additional dispositions that have emerged in this study. Whilst conducting this research I have been responsive to the context, the participants, and the data, whilst gaining a greater awareness of my place within UAE society.

Target Market(s)

Academic, research

Requirements
Must have
• Attractive Visuals
Nice to have
• Connections between the concepts

```html
<!DOCTYPE html>
<html lang="en">
<head>
<meta charset="utf-8">
<title>Teacher Educator Agility Framework</title>
<link href="https://fonts.googleapis.com/css2?family=Catamaran:wght@400;500;600&display=swap" rel="stylesheet">
<style>
  :root {
    --teal: #078d8f;
    --green: #7fab45;
    --orange: #e0a442;
    --ink: #5d6066;
    --rule: #d9dadd;
    --arrow: #7fb24a;
    --paper: #ffffff;
  }
  html, body {
    margin: 0;
    padding: 0;
    width: 1200px;
    height: 1200px;
    overflow: hidden;
    background: var(--paper);
  }
  .framework {
    display: block;
    width: 1200px;
    height: 1200px;
    font-family: "Catamaran", sans-serif;
  }
  .side-label { fill: var(--ink); font-size: 33px; font-weight: 500; text-anchor: middle; }
  .disposition { fill: var(--ink); font-size: 35px; font-weight: 500; text-anchor: middle; }
  .domain-label { fill: #ffffff; font-size: 34px; font-weight: 500; text-anchor: end; }
  .context-item { fill: var(--ink); font-size: 33px; font-weight: 500; }
  .context-bullet { fill: var(--arrow); }
  .cycle-label { fill: var(--ink); font-size: 33px; font-weight: 500; text-anchor: middle; }
  .empower-label { fill: #ffffff; font-size: 27px; font-weight: 600; text-anchor: middle; }
  .ring-teal { fill: var(--teal); }
  .ring-green { fill: var(--green); }
  .ring-orange { fill: var(--orange); }
  .quadrant-rule { stroke: var(--rule); stroke-width: 3; }
  .connector { stroke: var(--arrow); stroke-width: 2; fill: none; }
  .bracket { stroke: var(--green); stroke-width: 2; fill: none; }
</style>
</head>
<body>
<svg class="framework" viewBox="0 0 1920 1920" xmlns="http://www.w3.org/2000/svg" role="img" aria-label="Teacher educator agility framework">
  <defs>
    <radialGradient id="core-fill" cx="0.3" cy="0.2" r="0.9">
      <stop offset="0" stop-color="#e9eaec"/>
      <stop offset="0.6" stop-color="#f7f7f8"/>
      <stop offset="1" stop-color="#ffffff"/>
    </radialGradient>
    <filter id="soft-shadow" x="-20%" y="-20%" width="140%" height="140%">
      <feDropShadow dx="6" dy="10" stdDeviation="14" flood-color="#000" flood-opacity="0.16"/>
    </filter>
    <marker id="chevron" viewBox="0 0 10 10" refX="9" refY="5" markerWidth="9" markerHeight="9" orient="auto-start-reverse" markerUnits="userSpaceOnUse">
      <path d="M1 1 L9 5 L1 9" fill="none" stroke="#7fb24a" stroke-width="1.4"/>
    </marker>
  </defs>

  <!-- Side labels -->
  <text class="side-label" x="180" y="526">Time / Speed</text>
  <text class="side-label" x="180" y="570">Urgency</text>
  <text class="side-label" x="218" y="1422">Awareness of self</text>
  <text class="side-label" x="218" y="1466">Reflexivity</text>

  <!-- Concentric domains -->
  <g class="domains">
    <circle class="ring-teal" cx="603" cy="948" r="475" filter="url(#soft-shadow)"/>
    <path class="ring-teal" d="M760 1296 H1250 A43 43 0 0 1 1250 1382 H760 Z"/>
    <text class="domain-label" x="1255" y="1350">Inter-cultural Competence</text>

    <circle class="ring-green" cx="603" cy="948" r="420" filter="url(#soft-shadow)"/>
    <path class="ring-green" d="M960 790 H1247 A43 43 0 0 1 1247 876 H960 Z"/>
    <path class="ring-green" d="M980 981 H1247 A43 43 0 0 1 1247 1067 H980 Z"/>
    <text class="domain-label" x="1248" y="843">Context</text>
    <text class="domain-label" x="1254" y="1035">Relationships</text>

    <circle class="ring-orange" cx="603" cy="948" r="366" filter="url(#soft-shadow)"/>
    <path class="ring-orange" d="M720 605 H1247 A43 43 0 0 1 1247 691 H720 Z"/>
    <text class="domain-label" x="1249" y="659">Consumption of Research</text>

    <circle cx="603" cy="948" r="312" fill="#ffffff"/>
    <circle cx="603" cy="948" r="306" fill="url(#core-fill)"/>
  </g>

  <!-- Researcherly dispositions -->
  <g class="dispositions">
    <line class="quadrant-rule" x1="607" y1="755" x2="607" y2="1167"/>
    <line class="quadrant-rule" x1="334" y1="952" x2="880" y2="952"/>
    <text class="disposition" x="467" y="840">Sensory</text>
    <text class="disposition" x="467" y="877">Awareness</text>
    <text class="disposition" x="743" y="840">Value Deep</text>
    <text class="disposition" x="747" y="877">Understanding</text>
    <text class="disposition" x="470" y="1063">Responsiveness</text>
    <text class="disposition" x="747" y="1044">Cognitive</text>
    <text class="disposition" x="747" y="1081">Flexibility</text>
  </g>

  <!-- Context factors -->
  <g class="context-factors">
    <path class="bracket" d="M1290 832 H1360 M1360 750 V916"/>
    <circle class="context-bullet" cx="1392" cy="765" r="3"/>
    <circle class="context-bullet" cx="1392" cy="808" r="3"/>
    <circle class="context-bullet" cx="1392" cy="852" r="3"/>
    <circle class="context-bullet" cx="1392" cy="895" r="3"/>
    <text class="context-item" x="1404" y="777">Employment Contracts</text>
    <text class="context-item" x="1404" y="820">Cultural Differences</text>
    <text class="context-item" x="1404" y="864">Education Regulations</text>
    <text class="context-item" x="1404" y="907">Macro Economic Factors</text>
  </g>

  <!-- Relationship cycle -->
  <g class="relationship-cycle">
    <text class="cycle-label" x="1510" y="1048">Agency</text>
    <text class="cycle-label" x="1340" y="1150">Tacit</text>
    <text class="cycle-label" x="1340" y="1186">Knowledge</text>
    <text class="cycle-label" x="1663" y="1166">Tensions</text>
    <text class="cycle-label" x="1510" y="1276">Personal</text>
    <text class="cycle-label" x="1510" y="1311">Growth</text>

    <path class="connector" d="M1447 1153 H1575" marker-start="url(#chevron)" marker-end="url(#chevron)"/>
    <path class="connector" d="M1510 1090 V1216" marker-start="url(#chevron)" marker-end="url(#chevron)"/>
    <path class="connector" d="M1357 1097 V1038 H1418" marker-start="url(#chevron)" marker-end="url(#chevron)"/>
    <path class="connector" d="M1603 1041 H1663 V1099" marker-start="url(#chevron)" marker-end="url(#chevron)"/>
    <path class="connector" d="M1357 1216 V1273 H1418" marker-start="url(#chevron)" marker-end="url(#chevron)"/>
    <path class="connector" d="M1603 1275 H1663 V1218" marker-start="url(#chevron)" marker-end="url(#chevron)"/>
  </g>

  <!-- Personal empowerment arrow -->
  <g class="empowerment">
    <path fill="var(--green)" d="M1768 1037 H1746 L1795 966 L1845 1037 H1823 V1342 H1768 Z"/>
    <text class="empower-label" transform="translate(1804 1178) rotate(-90)">Personal Empowerment</text>
  </g>
</svg>
</body>
</html>
```